Training company needs a Quick Reference Card design

We have draft skeleton of the design and most of the text. But we need a designer to take it the rest if the way.
I have designed a 2 page quick reference card - it is meant to be a 2-sided document. The first page is portrait, the back page can either be portrait or landscape, I'm not too concerned, whichever fits best.
Section called 'Maps' on front, a map is a collection of documents (like a manual), a topic is a document (like a page or section of a manual) and a block is a section of a document. The graphic is mean to illustrate the hierarchy but essentially a map is a big document with smaller documents in it.
Please use the company's logo colors to differentiate the different sections with minimal/ highlight only use of the darkest color, preferably.
Please use the icons for the corresponding Information types in the chart of the back - except please re-design the icons color scheme to match the company's logo/website colors.

Target Market(s)

Technical writers, after attending our training course, as an ongoing resource for them

Industry/Entity Type

It Company

Font styles to use
Sans Serif

Requirements
Must have
• Must adhere to look and feel of brand/ website. www.lumarockwise.com
Nice to have
• Please keep the design modern and slick looking, not too busy, easy to read

```html
<!DOCTYPE html>
<html lang="en">
<head>
<meta charset="utf-8">
<title>Lumarockwise Quick Reference Card</title>
<link href="https://fonts.googleapis.com/css2?family=Arimo:wght@400;700&display=swap" rel="stylesheet">
<style>
  :root {
    --navy: #1c1a9a;
    --cyan: #00a5dc;
    --grey-line: #b4b4b4;
    --grey-text: #666;
    --ink: #1a1a1a;
    --band: #f5f5f7;
    --white: #fff;
  }
  * { box-sizing: border-box; margin: 0; padding: 0; }
  html, body { width: 927px; height: 1200px; overflow: hidden; background: var(--white); }
  body { font-family: "Arimo", Arial, sans-serif; color: var(--ink); position: relative; }
  .abs { position: absolute; }

  /* Header */
  .brand { left: 28px; top: 44px; display: flex; align-items: center; gap: 16px; }
  .brand-dot { width: 84px; height: 84px; border-radius: 50%; background: var(--cyan); }
  .brand-name { font-size: 34px; font-weight: 700; color: var(--navy); letter-spacing: 0.5px; }
  .card-title { right: 25px; top: 62px; font-size: 35px; font-weight: 700; color: var(--cyan); }
  .rule-cyan { left: 0; top: 164px; width: 512px; height: 13px; background: var(--cyan); }
  .rule-navy { left: 522px; top: 164px; width: 405px; height: 13px; background: var(--navy); }

  /* Hierarchy diagram */
  .map-frame { left: 54px; top: 210px; width: 369px; height: 248px; border: 1.5px solid var(--navy); }
  .map-label { position: absolute; top: 16px; width: 100%; text-align: center; font-weight: 700; font-size: 18px; color: var(--navy); }
  .topic-frame { position: absolute; top: 63px; width: 156px; height: 164px; border: 1.5px solid var(--cyan); }
  .topic-label { position: absolute; top: 18px; width: 100%; text-align: center; font-weight: 700; font-size: 16px; color: var(--cyan); }
  .block { position: absolute; left: 12px; width: 130px; height: 28px; border: 1.5px solid var(--grey-line);
           font-size: 15px; color: var(--grey-text); text-align: center; line-height: 25px; }
  .block.primary { top: 61px; }
  .block.sub { top: 111px; }

  .definition { left: 442px; width: 431px; padding: 9px 11px; font-size: 16px; line-height: 20px; }
  .definition b { font-weight: 700; }
  .def-map { top: 210px; height: 83px; border: 1.5px solid var(--navy); color: var(--navy); }
  .def-topic { top: 306px; height: 56px; border: 1.5px solid var(--cyan); color: var(--cyan); }
  .def-block { top: 376px; height: 82px; border: 1.5px solid var(--grey-line); color: var(--grey-text); }

  /* Bands */
  .band { left: 0; width: 927px; background: var(--band); }
  .band-rules { top: 486px; height: 228px; }
  .band-principles { top: 906px; height: 254px; }
  .section-title { width: 927px; left: 0; text-align: center; font-size: 19px; font-weight: 700; color: var(--navy); }

  .tip { border: 1.5px solid var(--cyan); background: var(--band); font-size: 16px; line-height: 20px; padding: 20px 13px 0; }
  .tip h3 { position: absolute; top: -11px; left: 14px; padding: 0 9px; background: var(--band);
            font-size: 16px; font-weight: 700; color: var(--cyan); line-height: 20px; }
  .rules-tip { top: 558px; width: 265px; height: 136px; }
  .principle-tip { top: 982px; width: 186px; height: 156px; padding-top: 22px; }

  /* Questions and language arts */
  .sub-title { top: 748px; font-size: 19px; font-weight: 700; color: var(--navy); }
  .questions { left: 68px; top: 790px; list-style: none; font-size: 15.5px; line-height: 25.5px; }
  .questions span { display: inline-block; width: 22px; }
  .divider { left: 539px; top: 742px; width: 2px; height: 136px; background: #ddd; }
  .divider-dot { left: 527px; top: 797px; width: 26px; height: 26px; border-radius: 50%; background: var(--white); border: 5px solid #ddd; }
  .arts { left: 596px; font-size: 16px; line-height: 20px; }
  .arts b { font-weight: 700; }
  .arts .hang { padding-left: 72px; }
</style>
</head>
<body>

<header>
  <div class="abs brand"><span class="brand-dot"></span><span class="brand-name">LUMAROCKWISE.com</span></div>
  <h1 class="abs card-title">Quick Reference Card</h1>
  <div class="abs rule-cyan"></div>
  <div class="abs rule-navy"></div>
</header>

<section class="hierarchy">
  <div class="abs map-frame">
    <div class="map-label">Map</div>
    <div class="topic-frame" style="left:19px">
      <div class="topic-label">Topic</div>
      <div class="block primary">Primary Block</div>
      <div class="block sub">Sub-Block</div>
    </div>
    <div class="topic-frame" style="left:192px">
      <div class="topic-label">Topic</div>
      <div class="block primary">Primary Block</div>
      <div class="block sub">Sub-Block</div>
    </div>
  </div>
  <p class="abs definition def-map"><b>A map</b> is a file that organizes topics into structured collections of information. Maps specify hierarchy and relationships among topics.</p>
  <p class="abs definition def-topic"><b>A topic</b> is a group of related blocks with a title. Use the chunking principle to group together relevant blocks.</p>
  <p class="abs definition def-block"><b>A block</b> is a bite-sized chunk of information about one main idea that allows the writer to organize the material into logical sections.</p>
</section>

<section class="writing-rules">
  <div class="abs band band-rules"></div>
  <h2 class="abs section-title" style="top:500px">General Writing Rules</h2>
  <div class="abs tip rules-tip" style="left:54px"><h3>Effective Sentences</h3>One main agent, action &amp; outcome. Use active voice and simplest tense possible. No more than 7 sentences per paragraph. Use lists and tables.</div>
  <div class="abs tip rules-tip" style="left:332px"><h3>Special Characters</h3>Avoid special characters, spell out words instead. Remove parentheses, colons and dashes. Avoid using quotation marks and slashes.</div>
  <div class="abs tip rules-tip" style="left:609px"><h3>Plain Language</h3>Write in short sentences. Provide useful titles. Use clear familiar words. Avoid excess words. Be consistent.</div>
</section>

<section class="before-writing">
  <h2 class="abs sub-title" style="left:70px">3 Questions to ask before you start writing:</h2>
  <ol class="abs questions">
    <li><span>1.</span>What is the purpose of this information?</li>
    <li><span>2.</span>What is the desired user response of this information?</li>
    <li><span>3.</span>Who is the audience?</li>
  </ol>
  <div class="abs divider"></div>
  <div class="abs divider-dot"></div>
  <h2 class="abs sub-title" style="left:596px">2 Types of Language Arts:</h2>
  <p class="abs arts" style="top:791px"><b>LAFI</b> – Language Arts for Information</p>
  <p class="abs arts" style="top:824px"><b>LAFPR</b> – Language Arts for Personal<br><span class="hang">Response</span></p>
</section>

<section class="principles">
  <div class="abs band band-principles"></div>
  <h2 class="abs section-title" style="top:924px">4 Cognitive Principles</h2>
  <div class="abs tip principle-tip" style="left:54px"><h3>Consistency</h3>Use similar terms and structures. Pick a term and stick with it. Use the same sequence of blocks. Use consistent styles.</div>
  <div class="abs tip principle-tip" style="left:266px"><h3>Chunking</h3>Maximum of nine (7 +/- 2) items in a list, rows in a table, blocks in a topic, or topics in a map.</div>
  <div class="abs tip principle-tip" style="left:477px;padding-top:24px"><h3>Relevance</h3>Group similar items together. Separate relevance? Separate block. Irrelevant? Delete it.</div>
  <div class="abs tip principle-tip" style="left:688px"><h3>Titling</h3>Name everything. Name every block, every topic, every map and every table column.</div>
</section>

</body>
</html>
```